Meadowlark Learning Growth Partners (MLGP)

This is a professional business card. Logo and picture are a must on the front of the card. I am an educational consultant. I have been consulting for the past three years for a company. I am now opening my own company. My goal for my consulting company is to eventually consult all over America.

Target Market(s)

Educators, schools, professionals

Industry/Entity Type

Consulting

Contact Information for Business Card

Picture/logo on front, simple modern design

Font styles to use
Serif

Colors
85abd2
0355a3
3176b5
cedeed

Requirements
Must have
• picture, logo,
• Odessa Pruitt, Ed.S
• address 5073 Cormorant ridge Dr. Nashville, TN 37940
• Cell:616-555-0148
• Office: 629-555-0172
• www.Mlgpedu.example
• pruittodessa@mailbox.example

```html
<!DOCTYPE html>
<html lang="en">
<head>
<meta charset="utf-8">
<title>MLGP - Odessa Pruitt - Business Card</title>
<link rel="stylesheet" href="https://fonts.googleapis.com/css2?family=Open+Sans:wght@400&family=Oswald:wght@600&display=swap">
<style>
  :root {
    --board: #ffffff;
    --card: #ede8da;
    --navy: #0b3a78;
    --ink: #1a1a1a;
    --photo-top: #3d7fd6;
    --photo-bottom: #2a5fb0;
    --label-font: "Open Sans", sans-serif;
    --card-font: "Oswald", serif;
  }
  * { margin: 0; padding: 0; box-sizing: border-box; }
  html, body { width: 1200px; height: 797px; overflow: hidden; background: var(--board); }
  .board { position: relative; width: 1200px; height: 797px; font-family: var(--label-font); color: var(--ink); }
  .board-title { position: absolute; left: 54px; top: 54px; font-size: 19px; line-height: 26px; }
  .card { position: absolute; top: 214px; width: 254px; height: 445px; background: var(--card); color: var(--navy); font-family: var(--card-font); font-weight: 600; text-align: center; }
  .card--front { left: 281px; }
  .card--back { left: 730px; }
  .card-label { position: absolute; top: 684px; width: 254px; text-align: center; font-size: 19px; }
  .card-label--front { left: 281px; }
  .card-label--back { left: 730px; }

  .brand { position: absolute; left: 18px; top: 22px; display: flex; align-items: center; height: 52px; }
  .brand-dot { width: 22px; height: 22px; border-radius: 50%; background: var(--navy); margin-right: 8px; }
  .brand-short { font-size: 22px; letter-spacing: 2px; margin-right: 8px; }
  .brand-rule { width: 1px; height: 50px; background: var(--navy); margin-right: 7px; }
  .brand-full { text-align: left; font-size: 10.5px; line-height: 13px; }

  .person-name { position: absolute; top: 96px; width: 100%; font-size: 20px; letter-spacing: 0.3px; }
  .portrait { position: absolute; left: 77px; top: 132px; width: 102px; height: 126px; background: linear-gradient(180deg, var(--photo-top), var(--photo-bottom)); }
  .address { position: absolute; top: 275px; width: 100%; font-size: 15px; line-height: 21px; }
  .phones { position: absolute; top: 331px; width: 100%; font-size: 16px; line-height: 19px; }
  .web { position: absolute; top: 390px; width: 100%; font-size: 15px; line-height: 20px; }

  .back-mark { position: absolute; left: 0; top: 0; width: 100%; height: 100%; }
  .back-dot { position: absolute; left: 72px; top: 92px; width: 110px; height: 110px; border-radius: 50%; background: var(--navy); }
  .back-name { position: absolute; top: 250px; width: 100%; font-size: 56px; letter-spacing: 6px; line-height: 70px; }
</style>
</head>
<body>
<main class="board">
  <div class="board-title">MLGP - Odessa Pruitt - Business Card<br>Design 4&nbsp; - Portrait</div>

  <section class="card card--front">
    <div class="brand">
      <span class="brand-dot"></span>
      <span class="brand-short">MLGP</span>
      <span class="brand-rule"></span>
      <span class="brand-full">Meadowlark<br>Learning<br>Growth<br>Partners</span>
    </div>
    <h1 class="person-name">Odessa Pruitt, Ed. S</h1>
    <div class="portrait" role="img" aria-label="Headshot portrait of Odessa Pruitt"></div>
    <p class="address">5073 Cormorant Ridge Drive<br>Nashville, TN 37940</p>
    <p class="phones">Cell: (616) 555-0148<br>Office: (629) 555-0172</p>
    <p class="web">www.mlgpedu.example<br>pruittodessa@mailbox.example</p>
  </section>

  <section class="card card--back">
    <div class="back-mark">
      <span class="back-dot"></span>
      <div class="back-name">MLGP</div>
    </div>
  </section>

  <div class="card-label card-label--front">Front</div>
  <div class="card-label card-label--back">Back</div>
</main>
</body>
</html>
```